Lens Harbor Teutonia Website - Photography and Films

We are looking for a design that expresses the friendly, open nature of our company Lens Harbor Teutonia, yet at the same time is professional looking and functional.

Lens Harbor Teutonia is a B2B focused operation that hires out multi-lingual camera crews (and equipment) throughout Germany and Europe. We also produce tv features and coporate films. Our unique selling point is that we are native English speakers who can communicate with our international clients (usually British or American) and organise the logistics of shooting in foreign countries.

For content inspiration, see our current website: http://www.lensharborteutonia.com - however we want to move away from the very simple structure of this site and move towards a layout that displays and allows for frequently updated content (e.g. in the form of a blog).

Here is an example of the kind of clean look we like:
http://www.qrvpixelarchive.com/archive/main/reelsqrv.do#reel=48213760

Please keep within the following specifications:
- We wish to keep our logo (grey/white, font: Glypha) and our company colour red (#C40A0A) as they are.
- Maximum Width 960px, on a large browser-window the design should be centred
- Easily readable font sizes with good contrast
- Provide your design in PSD file format
- Our logo should be graphically displayed in the top left of the header.
- The design should allow space for a video.
- The page should have a clearly recognisable end in the form of a footer.

The following menu items need to be clearly arranged so the viewer is not overwhelmed or confused:
About
Services - Crews / Corporate Shoots / Webcasts / Production Arm / Legal Videography
Recent Productions
Blog
Testimonials
Get a Quote
Contact
Film Library
Showreel
Events
Film Location Guide - Frankfurt / Cologne / Zurich / Helsinki / Amsterdam / London / Paris / Rome / Brussels / Berlin / Munich
Updates

Reason: Hi - thanks very much for your interest in our design project.  We are extending this auction because we haven't had enough time to really focus on the desigs and provide immediate feedback to designers.  We will try to provide timely feedback and are giving you more time to make any adjustments to your designs etc.
Thanks!
Marla

Target Market(s)

Our target customers are males and females between 25 and 55 years (mostly British and American). More important than their demographic though, is their occupation - they are largely communication and design savvy individuals belonging to one of the following three categories: 1)Broadcasters (usually producers for example from the QRV or Horizon Vista TV seeking trustworthy, affordable crews for their foreign shoots).

2) Video Production Companies (seeking a trustworthy, affordable partner company to provide the crews for their own corporate clients).

3) Corporate Communications Specialists (seeking professional producers and crews to facilitate production of company videos or filming of events).

Industry/Entity Type

Camera

Requirements
Must have
• A fresh clean appearance with good use of white space.
Should not have
• Avoid dark heavy colours and designs.
• Avoid designs that would be impractical and could potentially take a long time to load.

```html
<!DOCTYPE html>
<html lang="en">
<head>
<meta charset="utf-8">
<title>Lens Harbor Teutonia</title>
<link href="https://fonts.googleapis.com/css2?family=Roboto+Slab:wght@700&family=Arvo&family=Tinos&family=Arimo&family=Pathway+Gothic+One&display=swap" rel="stylesheet">
<style>
:root{
  --brand-red:#c40a0a;
  --deep-red:#8d0707;
  --text:#5a5a5a;
  --heading:#2a2a2a;
  --rule:#bbb;
  --footer-bg:#2b2b2b;
  --footer-text:#e4e4e4;
  --footer-bar:#6a6a6a;
  --white:#fff;
}
*{margin:0;padding:0;box-sizing:border-box}
html,body{width:990px;height:1200px;overflow:hidden;background:var(--white)}
body{position:relative;font-family:"Arimo",Arial,sans-serif;color:var(--text)}
.abs{position:absolute}

.site-header{position:absolute;left:0;top:0;width:990px;height:58px;background:linear-gradient(#d41414,#b00808)}
.logo{position:absolute;left:104px;top:6px;font-family:"Roboto Slab",serif;font-weight:700;font-size:33px;line-height:40px;color:var(--white);letter-spacing:-0.5px;white-space:nowrap}
.header-contact{position:absolute;right:98px;top:9px;text-align:right;color:var(--deep-red);font-family:"Pathway Gothic One",sans-serif;white-space:nowrap}
.header-contact .phone{font-size:24px;line-height:24px;letter-spacing:1px}
.header-contact .mail{font-size:13px;line-height:16px;letter-spacing:.5px}

.hero{position:absolute;left:0;top:58px;width:990px;height:309px;background:linear-gradient(#9a9a9a,#7d7d7d 60%,#888)}
.hero-stage{position:absolute;left:97px;top:0;width:795px;height:309px;background:linear-gradient(90deg,#3f3f3f,#8e8e8e 45%,#b8b8b8 75%,#a7a7a7)}
.hero-photo{position:absolute;left:0;top:0;width:470px;height:309px;background:radial-gradient(ellipse at 40% 45%,#d8d8d8,#6a6a6a 55%,#2c2c2c)}
.slider-dots{position:absolute;right:8px;top:8px;display:flex;gap:5px}
.slider-dots span{width:20px;height:20px;border-radius:50%;background:#666;border:2px solid #999}
.slider-dots span.active{background:var(--deep-red);border-color:#b33}
.hero-title{position:absolute;left:448px;top:70px;font-family:"Arvo",serif;font-size:29px;line-height:36px;letter-spacing:3px;color:#7a7a7a;text-shadow:1px 1px 0 #d6d6d6,-1px -1px 0 #555;white-space:nowrap}
.quick-links{position:absolute;right:0;bottom:0;width:385px;height:27px;background:var(--brand-red);color:var(--white);font-size:12px;letter-spacing:1px;display:flex;align-items:center;justify-content:center;gap:12px;white-space:nowrap}

.main-nav{position:absolute;left:0;top:367px;width:990px;height:62px;background:linear-gradient(#8e8e8e,#6f6f6f)}
.main-nav ul{position:absolute;left:97px;top:0;width:795px;height:62px;list-style:none;display:flex;justify-content:space-between}
.main-nav li{font-family:"Tinos",serif;font-size:15px;color:#1e1e1e;line-height:62px;padding:0 9px;white-space:nowrap}
.main-nav li.current{background:var(--brand-red);color:var(--white)}

h2{font-family:"Pathway Gothic One",sans-serif;font-weight:400;font-size:28px;line-height:30px;color:var(--heading);letter-spacing:.5px;white-space:nowrap}
.content p{font-size:10.5px;line-height:15px;text-align:justify}
.content p + p{margin-top:15px}
.rule{position:absolute;border-top:1px dotted var(--rule)}
.col-divider{position:absolute;left:639px;top:452px;height:462px;border-left:1px dotted var(--rule)}
.client-box{position:absolute;left:661px;top:490px;width:231px;height:133px;border:1px solid #ddd}

.site-footer{position:absolute;left:0;top:938px;width:990px;height:262px;background:var(--footer-bg);color:var(--footer-text)}
.site-footer h3{position:absolute;font-family:"Pathway Gothic One",sans-serif;font-weight:400;font-size:27px;color:#d8d8d8;letter-spacing:.5px}
.bar{position:absolute;height:5px;background:var(--footer-bar)}
.vsep{position:absolute;top:55px;height:190px;border-left:1px solid #444}
.sitemap-col{position:absolute;top:64px;list-style:none;font-size:10px;line-height:15px;letter-spacing:.6px;white-space:nowrap}
.sitemap-col li.top::before{content:"» ";font-size:9px}
.sitemap-col li.sub{padding-left:8px}
.sitemap-col li.sub::before{content:"▪ ";font-size:7px}
.contact-text{position:absolute;left:530px;top:64px;font-size:10px;line-height:15px;letter-spacing:.6px;white-space:nowrap}
.social{position:absolute;top:66px;width:34px;height:34px;background:linear-gradient(#8a8a8a,#5e5e5e);border-radius:3px;font-size:7.5px;color:var(--white);display:flex;align-items:center;justify-content:center}
.thin{position:absolute;left:773px;top:114px;width:118px;border-top:1px solid #555}
.c-icon{position:absolute;left:773px;top:126px;width:12px;height:18px;border:1px solid #ccc;font-size:10px;line-height:16px;text-align:center;color:#ddd}
.imprint{position:absolute;left:773px;top:169px;width:130px;font-size:8.5px;line-height:14px;white-space:nowrap}
</style>
</head>
<body>

<header class="site-header">
  <div class="logo">lensharborteutonia</div>
  <div class="header-contact">
    <div class="phone">+49-69-417250</div>
    <div class="mail">info@lens-harbor-teutonia.com</div>
  </div>
</header>

<section class="hero">
  <div class="hero-stage">
    <div class="hero-photo" role="img" aria-label="Black and white photo of a cameraman filming with a video camera"></div>
    <div class="slider-dots"><span class="active"></span><span></span><span></span></div>
    <div class="hero-title">English Speaking<br>Camera Crews<br>throughout<br>Germany &amp; Europe</div>
    <div class="quick-links"><span>Recent Productions</span><span>|</span><span>Film Library</span><span>|</span><span>Film Location Guide</span></div>
  </div>
</section>

<nav class="main-nav">
  <ul>
    <li class="current">HOME</li><li>ABOUT</li><li>SERVICES</li><li>BLOG</li><li>TESTIMONIALS</li><li>GET A QUOTE</li><li>CONTACT</li><li>SHOWREEL</li><li>EVENTS</li>
  </ul>
</nav>

<main class="content">
  <section class="abs" style="left:97px;top:452px;width:521px">
    <h2>WELCOME TO CAMERA CREWS</h2>
    <p style="margin-top:8px">30 years ago, Arno Wexley set up lens harbor teutonia to Lorem ipsum dolor sit amet, consetetur sadipscing elitr, sed diam nonumy eirmod tempor invidunt ut labore et dolore magna aliquyam ...</p>
  </section>
  <div class="rule" style="left:97px;top:539px;width:519px"></div>

  <section class="abs" style="left:97px;top:561px;width:521px">
    <h2>LOREM IPSUM</h2>
    <p style="margin-top:7px">Lorem Ipsum is simply dummy text of the printing and typesetting industry. Lorem Ipsum has been the industry's standard dummy text ever since the 1500s, when an unknown printer took a galley of type and scrambled it to make a type specimen book.</p>
    <p>It has survived not only five centuries, but also the leap into electronic typesetting, remaining essentially unchanged. It was popularised in the 1960s with the release of Typerite sheets containing Lorem Ipsum passages, and more recently with desktop publishing software like Quillset Layout including versions of Lorem Ipsum.</p>
  </section>
  <div class="rule" style="left:97px;top:737px;width:519px"></div>

  <section class="abs" style="left:97px;top:763px;width:521px">
    <h2>LOREM IPSUM</h2>
    <p style="margin-top:6px">Lorem Ipsum is simply dummy text of the printing and typesetting industry. Lorem Ipsum has been the industry's standard dummy text ever since the 1500s, when an unknown printer took a galley of type and scrambled it to make a type specimen book.</p>
    <p>It has survived not only five centuries, but also the leap into electronic typesetting, remaining essentially unchanged. It was popularised in the 1960s with the release of Typerite sheets containing Lorem Ipsum passages, and more recently with desktop publishing software like Quillset Layout including versions of Lorem Ipsum.</p>
  </section>

  <div class="col-divider"></div>

  <h2 class="abs" style="left:660px;top:452px">OUR CLIENTS</h2>
  <div class="client-box"></div>
  <div class="rule" style="left:660px;top:648px;width:230px"></div>

  <section class="abs" style="left:660px;top:667px;width:232px">
    <h2>NEWS / EVENTS</h2>
    <p style="margin-top:8px">Donec viverra augue dictum diam malesuada laoreet mattis massa volutpat.</p>
    <p>Ut eleifend neque et risus commodo elementum pulvinar quis ipsum.</p>
    <p>Curabitur vestibulum auctor eros, quis dignissim velit blandit id.</p>
    <p>Curabitur tempus nunc id mauris feugiat in varius erat elementum.</p>
    <p>Praesent tempor libero sed leo lobortis a rhoncus felis convallis.</p>
  </section>
</main>

<footer class="site-footer">
  <h3 style="left:97px;top:14px">SITEMAP</h3>
  <div class="bar" style="left:97px;top:46px;width:372px"></div>
  <ul class="sitemap-col" style="left:97px">
    <li class="top">About</li><li class="top">Recent Productions</li><li class="top">Blog</li><li class="top">Testimonials</li><li class="top">Get a Quote</li><li class="top">Contact</li><li class="top">Film Library</li><li class="top">Showreel</li><li class="top">Events</li><li class="top">Sitemap</li><li class="top">Disclaimer</li>
  </ul>
  <ul class="sitemap-col" style="left:233px">
    <li class="top">Film Location Guide</li><li class="sub">Frankfurt</li><li class="sub">Cologne</li><li class="sub">Zurich</li><li class="sub">Helsinki</li><li class="sub">Amsterdam</li><li class="sub">London</li><li class="sub">Paris</li><li class="sub">Rome</li><li class="sub">Brussels</li><li class="sub">Berlin</li><li class="sub">Munich</li>
  </ul>
  <ul class="sitemap-col" style="left:365px">
    <li class="top">Services</li><li class="sub">Crews</li><li class="sub">Corporate Shoots</li><li class="sub">Webcasts</li><li class="sub">Production Arm</li><li class="sub">Legal Videography</li>
  </ul>

  <div class="vsep" style="left:499px"></div>

  <h3 style="left:530px;top:14px">CONTACT</h3>
  <div class="bar" style="left:530px;top:46px;width:179px"></div>
  <div class="contact-text">
    Lens Harbor Teutonia<br>c/o Wexley Pictures GmbH<br>Kastanienweg 18<br>D-60311 Frankfurt<br>Germany<br><br>
    Tel.: +49-69-417250<br>Fax: +49-69-417251<br>Toll free from the USA 1-866-555-0142<br>info@lens-harbor-teutonia.com<br>www.lensharborteutonia.com
  </div>

  <div class="vsep" style="left:742px"></div>

  <h3 style="left:773px;top:14px">JOIN US</h3>
  <div class="bar" style="left:773px;top:46px;width:118px"></div>
  <div class="social" style="left:773px">Circlo</div>
  <div class="social" style="left:815px">Murmur</div>
  <div class="social" style="left:857px">Workweb</div>
  <div class="thin"></div>
  <div class="c-icon">c</div>
  <div class="bar" style="left:773px;top:155px;width:118px"></div>
  <div class="imprint">© wexley pictures<br>Kastanienweg 18 ▪ 60311<br>Frankfurt/Main ▪ Germany ▪<br>info@wexley-pictures.com<br>Tel.: +49-69-417250 ▪ Toll</div>
</footer>

</body>
</html>
```